Brit Rock covers band "The Tin Kettles" requires poster for Marlowe Lounge Friday March 31st

I want a design for a poster (A3 and A4) and Facebook/Instagram ads.
Primary focus is the band name logo "The Tin Kettles", style as in attached file, followed by tag "Old Skool Brit Rock".
Backdrop to be 60's psychedelic art.
Secondary focus is the venue "The Marlowe Lounge"
Supporting text to include:
- 27 Fenwick Road, Chatswood SYDNEY
- Friday 31st March 2023
- 7:00 pm until late
- Bar sales refreshments
- NO admission fee

```html
<!DOCTYPE html>
<html lang="en">
<head>
<meta charset="utf-8">
<title>The Tin Kettles – Marlowe Lounge</title>
<link rel="stylesheet" href="https://fonts.googleapis.com/css2?family=Anton&family=Oswald:wght@700&display=swap">
<style>
  :root {
    --vinyl-dark: #1c1c22;
    --vinyl-mid: #33333c;
    --paper: #ffffff;
    --rock-red: #e31d25;
    --navy: #232b73;
    --ink: #0d0d0d;
    --flag-blue: #27327f;
  }
  * { margin: 0; padding: 0; box-sizing: border-box; }
  html, body { width: 848px; height: 1200px; overflow: hidden; background: var(--vinyl-dark); }
  .poster { position: relative; width: 848px; height: 1200px; overflow: hidden; }
  .record-backdrop {
    position: absolute; inset: 0;
    background:
      radial-gradient(circle at 20% 15%, rgba(240,130,40,.25), transparent 30%),
      radial-gradient(circle at 80% 30%, rgba(90,160,210,.22), transparent 30%),
      radial-gradient(circle at 15% 65%, rgba(220,70,160,.2), transparent 28%),
      radial-gradient(circle at 55% 75%, rgba(240,190,40,.2), transparent 28%),
      radial-gradient(circle at 85% 90%, rgba(70,170,90,.2), transparent 28%),
      linear-gradient(160deg, var(--vinyl-mid), var(--vinyl-dark));
  }
  .band-name {
    position: absolute; left: 100px; top: 196px; width: 680px;
    font-family: "Anton", sans-serif; color: var(--paper);
    text-transform: uppercase; line-height: .92;
  }
  .band-name .line-one { display: block; font-size: 196px; letter-spacing: -2px; }
  .band-name .line-two { display: block; font-size: 196px; letter-spacing: -2px; margin-left: 14px; }
  .tag-badge { position: absolute; left: 538px; top: 530px; width: 240px; height: 240px; }
  .tag-badge .tag-text {
    position: absolute; inset: 0; display: flex; flex-direction: column;
    align-items: center; justify-content: center;
    font-family: "Anton", sans-serif; color: var(--paper); font-size: 40px; line-height: 1.05;
    text-transform: uppercase;
  }
  .event-info { position: absolute; left: 102px; top: 781px; }
  .info-box {
    display: block; width: max-content; background: var(--paper);
    font-family: "Oswald", sans-serif; font-weight: 700;
    box-shadow: 4px 5px 6px rgba(0,0,0,.45);
    padding: 0 14px; margin-bottom: 7px; line-height: 1.18;
  }
  .venue { color: var(--rock-red); font-size: 52px; padding-right: 20px; }
  .address { color: var(--rock-red); font-size: 24px; margin-top: 8px; padding: 3px 14px 2px 10px; }
  .date { color: var(--navy); font-size: 52px; }
  .time { color: var(--navy); font-size: 52px; padding-right: 16px; }
  .extras { color: var(--ink); font-size: 27px; padding: 3px 14px; }
</style>
</head>
<body>
<main class="poster">
  <div class="record-backdrop" role="img" aria-label="Backdrop of scattered vinyl 45 records with colourful centre labels"></div>

  <h1 class="band-name">
    <span class="line-one">The Tin</span>
    <span class="line-two">Kettles</span>
  </h1>

  <div class="tag-badge">
    <svg width="240" height="240" viewBox="0 0 240 240" role="img" aria-label="Round British flag badge">
      <defs>
        <radialGradient id="flagTone" cx="50%" cy="50%" r="50%">
          <stop offset="0" stop-color="#e31d25"/>
          <stop offset=".55" stop-color="#c94a5a"/>
          <stop offset="1" stop-color="#27327f"/>
        </radialGradient>
      </defs>
      <circle cx="120" cy="120" r="120" fill="url(#flagTone)"/>
    </svg>
    <p class="tag-text"><span>Old Skool</span><span>Brit Rock</span></p>
  </div>

  <section class="event-info">
    <p class="info-box venue">The Marlowe Lounge</p>
    <p class="info-box address">- 27 Fenwick Road, Chatswood SYDNEY</p>
    <p class="info-box date">Friday 31st March 2023</p>
    <p class="info-box time">7:00 pm until late</p>
    <p class="info-box extras">Bar sales refreshments | NO admission fee</p>
  </section>
</main>
</body>
</html>
```